Business Card Design

This is a coaching and training company. We deliver personal development workshops, training and one to one coaching. We would like the current logo to be used.

Target Market(s)

For coaches, small business owners and people aged around 40-60 who are seeking direction in their life

Industry/Entity Type

Training

Contact Information for Business Card

Marion Tuckett
Speaker-Trainer-Coach
There is no going back ...
0461 738196
18 Harrow Lane Pembry
mtuckett47@quillbox.net

Font styles to use
Sans Serif

Requirements
Should not have
• No old style fonts

```html
<!DOCTYPE html>
<html lang="en">
<head>
<meta charset="utf-8">
<title>Crossway Business Card – Option 2</title>
<link href="https://fonts.googleapis.com/css2?family=Questrial&display=swap" rel="stylesheet">
<style>
  :root {
    --board-grey: #bcbdbf;
    --card-white: #ffffff;
    --brand-blue: #25a9e0;
    --ink: #231f20;
    --mark-light: #eeeff0;
    --mark-shade: #d9dadc;
  }
  * { margin: 0; padding: 0; box-sizing: border-box; }
  html, body { width: 953px; height: 1200px; overflow: hidden; }
  body {
    position: relative;
    background: var(--board-grey);
    font-family: "Questrial", Arial, sans-serif;
    color: var(--ink);
  }
  .card {
    position: absolute;
    left: 73px;
    width: 798px;
    height: 491px;
  }
  .card--front { top: 68px; background: var(--card-white); }
  .card--back { top: 598px; background: var(--brand-blue); }

  .contact__line {
    position: absolute;
    left: 0; right: 0;
    text-align: center;
    font-size: 22px;
    line-height: 28px;
    white-space: nowrap;
  }
  .contact__line--name { top: 78px; }
  .contact__line--role { top: 103px; color: var(--brand-blue); }
  .contact__line--tagline { top: 128px; font-size: 15px; line-height: 22px; color: var(--ink); }
  .contact__line--phone { top: 153px; }
  .contact__line--address { top: 180px; }
  .contact__line--email { top: 227px; color: var(--brand-blue); }

  .brand { position: absolute; left: 0; right: 0; text-align: center; }
  .brand__square { display: block; margin: 0 auto; background: linear-gradient(180deg, var(--mark-light), var(--mark-shade)); }
  .brand__name { display: block; letter-spacing: 0.5px; }

  .brand--small { top: 299px; }
  .brand--small .brand__square { width: 97px; height: 81px; }
  .brand--small .brand__name { margin-top: 3px; font-size: 18px; line-height: 20px; color: var(--brand-blue); }
  .brand--small .brand__tagline { display: block; font-size: 9px; line-height: 12px; color: var(--ink); }

  .brand--large { top: 70px; }
  .brand--large .brand__square { width: 291px; height: 249px; background: linear-gradient(180deg, #ffffff, var(--mark-light)); }
  .brand--large .brand__name { margin-top: 16px; font-size: 52px; line-height: 58px; color: var(--card-white); }
  .brand--large .brand__rule { width: 292px; height: 3px; margin: 4px auto 6px; background: var(--card-white); }
  .brand--large .brand__tagline { display: block; font-size: 19px; line-height: 24px; color: var(--card-white); }

  .spec {
    position: absolute;
    left: 75px; top: 1105px;
    font-size: 30px;
    line-height: 40px;
    color: var(--ink);
  }
</style>
</head>
<body>
  <section class="card card--front">
    <p class="contact__line contact__line--name">Marion Tuckett Speaker</p>
    <p class="contact__line contact__line--role">Trainer-Coach</p>
    <p class="contact__line contact__line--tagline">There is no going back ...</p>
    <p class="contact__line contact__line--phone">0461 738196 18</p>
    <p class="contact__line contact__line--address">Harrow Lane Pembry</p>
    <p class="contact__line contact__line--email">mtuckett47@quillbox.net</p>
    <div class="brand brand--small">
      <span class="brand__square"></span>
      <span class="brand__name">CROSSWAY</span>
      <span class="brand__tagline">Coaching and Training Solutions</span>
    </div>
  </section>

  <section class="card card--back">
    <div class="brand brand--large">
      <span class="brand__square"></span>
      <span class="brand__name">CROSSWAY</span>
      <div class="brand__rule"></div>
      <span class="brand__tagline">Coaching and Training Solutions</span>
    </div>
  </section>

  <div class="spec">
    <p>Option 2</p>
    <p>SIZE: 94mm x 58mm</p>
  </div>
</body>
</html>
```